Vantor Reach Unique Marketing Website Design

I am starting a new company that is a thought leader in the marketing consulting space. The company is called Vantor Reach. We intend to build a Wordpress site on the Astra Theme with the Spectra builder. Our goal is to become the leading voice that empowers high-ticket service business leaders to become Vantor Reach by equipping them with the cutting-edge frameworks and decision grade intelligence taught in leading business schools. What we are looking for is a website design that is clean and professional, making some use of white space well also being eye catching and distinctive in the consulting space. We will probably want to have a video on the homepage not in the hero section, but just below to explain the company and what we do. Our tagline is "Be found. Be chosen." I have attached a brand guide with some messaging, our typography choices, and our color system. The full site will have a primary nav that is four pages - About us, Services, Insights (essentially a blog), and Contact Us. The goal of this project is to develop an art direction that I can give to a designer to build loads of new pages.

Target Market(s)

Business owners (mostly male) from 30-60 years old, looking to fix their sales and marketing funnel.

Industry/Entity Type

Marketing consulting

Font styles to use
Sans Serif

Requirements
Must have
• A clean, professional design that builds trust with owners of high-ticket service businesses. We need a space for explainer video, and sections that tell prospects what we do. Would also like to have a blog carousel.
Nice to have
• Social feeds, if possible. See attached documents for colors and fonts.
Should not have
• Our feel is professional enough to be trustworthy, but unique enough to be memorable. Cartoon ideas do not meet the professional test, and we do not want the website to appear feminine.

```html
<!DOCTYPE html>
<html lang="en">
<head>
<meta charset="utf-8">
<title>Vantor Reach — Be found. Be chosen.</title>
<link href="https://fonts.googleapis.com/css2?family=Roboto:wght@300;400;500;700&display=swap" rel="stylesheet">
<style>
:root{
  --blue:#3559e0;
  --blue-deep:#2c49c9;
  --navy:#2a2370;
  --ink:#222428;
  --muted:#555a63;
  --soft:#f1f2f8;
  --line:#c9ccd6;
  --footer:#333333;
  --white:#ffffff;
}
*{box-sizing:border-box;margin:0;padding:0}
html,body{width:1200px;height:4587px;overflow:hidden}
body{position:relative;background:var(--white);font-family:'Roboto',Arial,sans-serif;color:var(--ink)}
.abs{position:absolute}
.accent{color:var(--blue);font-weight:700}
.btn-outline{position:absolute;border:2px solid var(--blue);border-radius:30px;color:var(--ink);background:#fff;display:flex;align-items:center;justify-content:center;font-size:17px}
.backdrop{position:absolute;left:0;top:0}

/* nav */
.brand{position:absolute;font-weight:700;font-size:29px;color:var(--ink);display:flex;align-items:center;gap:10px}
.brand .dot{width:12px;height:12px;background:var(--blue);display:inline-block}
.nav{position:absolute;top:48px;left:560px;display:flex;gap:30px;font-size:17px;color:#fff;text-shadow:0 1px 3px rgba(0,0,0,.35)}
.nav-cta{position:absolute;left:995px;top:38px;width:153px;height:44px;border-radius:24px;background:#fff;color:var(--blue-deep);font-size:17px;display:flex;align-items:center;justify-content:center}

/* hero */
.hero-title{left:68px;top:228px;font-size:46px;font-weight:400;color:var(--ink)}
.hero-lead{left:68px;top:298px;font-size:21px;color:var(--ink)}
.hero-text{left:68px;top:356px;font-size:19px;line-height:30px;color:var(--ink)}

/* about */
.video-card{position:absolute;left:142px;top:755px;width:445px;height:366px;background:#fff;border-radius:10px;box-shadow:0 6px 22px rgba(40,50,90,.18);padding:10px}
.video-card .media{width:100%;height:100%;border-radius:6px;background:linear-gradient(135deg,#d9dde6,#f4f5f9 60%,#e5e9f2)}
.video-frame{position:absolute;left:206px;top:783px;width:413px;height:369px;border:5px solid var(--navy);border-radius:0 14px 14px 14px}
.play{position:absolute;left:321px;top:894px;width:86px;height:86px;border-radius:50%;background:#2b2b2b}
.video-label{position:absolute;left:270px;top:1006px;font-size:25px;font-weight:700;color:#333}
.section-title{position:absolute;font-size:43px;font-weight:400;color:var(--ink)}
.bar-mark{display:inline-block;width:3px;height:38px;border-left:3px solid var(--ink);border-right:3px solid var(--ink);margin-right:16px;vertical-align:-4px}
.about-copy{left:688px;top:832px;width:405px;font-size:14.5px;line-height:24px;color:#333}
.about-copy strong{font-weight:500}
.about-copy p+p{margin-top:20px}

/* services */
.eyebrow{position:absolute;width:1200px;text-align:center;font-size:30px;color:var(--ink)}
.service-title{position:absolute;font-size:28px;font-weight:500;color:var(--ink)}
.facts{position:absolute;width:500px}
.fact{margin-bottom:19px}
.fact h4{font-size:19px;font-weight:500;color:var(--ink);display:flex;align-items:center;gap:8px}
.fact p{font-size:14.5px;line-height:22px;color:var(--muted);padding-left:27px;margin-top:6px}
.tick{width:18px;height:18px;flex:none}
.block{position:absolute;background:var(--blue)}
.photo{position:absolute}

/* cta */
.cta-kicker{left:557px;top:2622px;font-size:32px;font-weight:500;color:#fff}
.cta-head{left:557px;top:2668px;font-size:46px;font-weight:300;line-height:56px;color:#fff}
.cta-btn{position:absolute;left:559px;top:2823px;width:197px;height:48px;border-radius:26px;background:#fff;color:var(--blue-deep);font-size:19px;font-weight:500;display:flex;align-items:center;justify-content:center}
.cta-photo{position:absolute;left:930px;top:2500px;width:200px;height:505px;background:linear-gradient(180deg,rgba(255,255,255,.10),rgba(255,255,255,.03))}

/* blog */
.card{position:absolute;top:3172px;width:288px;height:381px;background:#fff;box-shadow:0 4px 18px rgba(40,50,90,.12)}
.card .thumb{height:174px}
.card .body{padding:20px 23px}
.card .by{font-size:12px;color:var(--muted)}
.card h3{font-size:16.5px;font-weight:400;line-height:22px;margin-top:10px;color:var(--ink)}
.card p{font-size:13.5px;line-height:19.5px;color:var(--muted);margin-top:10px;max-width:232px}
.card a{display:inline-block;font-size:13.5px;color:var(--blue-deep);text-decoration:underline;margin-top:10px}
.btn-dark{position:absolute;left:502px;top:3594px;width:196px;height:50px;border-radius:26px;background:#333;color:#fff;font-size:16px;display:flex;align-items:center;justify-content:center;box-shadow:0 4px 10px rgba(0,0,0,.2)}

/* contact */
.contact-title{position:absolute;width:1200px;top:3806px;text-align:center;font-size:44px;font-weight:500;color:var(--navy)}
.field{position:absolute;border:1.5px solid var(--line);background:#fff;font-size:17px;color:#555;padding:10px 17px}
.send{position:absolute;left:516px;top:4121px;width:168px;height:46px;border:2px solid var(--blue);border-radius:26px;font-size:19px;font-weight:500;display:flex;align-items:center;justify-content:center;color:var(--ink)}

/* footer */
.footer{position:absolute;left:0;top:4236px;width:1200px;height:351px;background:var(--footer);color:#fff}
.footer-brand{position:absolute;left:134px;top:136px;width:258px;height:46px;background:#fff;color:var(--ink);font-size:27px;font-weight:700;display:flex;align-items:center;justify-content:center}
.footer h5{position:absolute;font-size:20px;font-weight:400;letter-spacing:.5px}
.footer-links{position:absolute;left:473px;top:98px;list-style:none;font-size:14px;line-height:28.5px;color:#d0d0d0}
.footer-links li::before{content:"›";color:#888;margin-right:8px}
.footer-links li:first-child{color:#fff}
.sub-note{position:absolute;left:723px;top:90px;font-size:15px;color:#cfcfcf}
.sub-form{position:absolute;left:721px;top:127px;width:347px;height:36px;border-radius:20px;background:#fff;overflow:hidden;display:flex}
.sub-form span{flex:1;font-size:14px;color:#777;padding:10px 24px}
.sub-form b{width:126px;background:var(--blue);color:#fff;font-weight:400;font-size:15px;display:flex;align-items:center;justify-content:center}
.social{position:absolute;left:722px;top:204px;display:flex;gap:7px}
.social i{width:36px;height:36px;border:1.5px solid #fff;border-radius:50%}
.copyright{position:absolute;width:1200px;top:304px;text-align:center;font-size:14px;color:#bdbdbd}
.copyright b{color:#fff;font-weight:400}
</style>
</head>
<body>

<!-- page backgrounds -->
<svg class="backdrop" width="1200" height="4587" viewBox="0 0 1200 4587" aria-hidden="true">
  <defs>
    <linearGradient id="heroPhoto" x1="0" y1="0" x2="1" y2="1">
      <stop offset="0" stop-color="#56627a"/>
      <stop offset=".5" stop-color="#4a566e"/>
      <stop offset="1" stop-color="#aeb6c6"/>
    </linearGradient>
    <linearGradient id="ctaBand" x1="0" y1="0" x2="1" y2="0">
      <stop offset="0" stop-color="#3c61e6"/>
      <stop offset="1" stop-color="#3355dc"/>
    </linearGradient>
  </defs>
  <rect x="0" y="0" width="1200" height="640" fill="#f3f4f9"/>
  <path d="M0 640 L1200 640 L1200 720 C900 640 500 660 0 620 Z" fill="#fff"/>
  <path d="M0 960 C250 1000 500 1060 800 1120 C1000 1160 1120 1200 1200 1190 L1200 700 C900 640 500 680 0 690 Z" fill="var(--soft)"/>
  <path d="M0 640 L0 990 C300 1030 600 1110 900 1170 C1050 1200 1150 1230 1200 1210 L1200 1226 C1100 1240 980 1225 850 1200 C550 1140 300 1060 0 1010 Z" fill="#fff"/>
  <path d="M0 2370 C200 2440 420 2470 700 2440 C900 2415 1060 2425 1200 2418 L1200 3005 L0 3005 Z" fill="url(#ctaBand)"/>
  <rect x="0" y="3005" width="1200" height="700" fill="#f3f4f8"/>
  <path d="M0 3700 C300 3740 600 3690 900 3730 C1050 3750 1150 3720 1200 3700 L1200 3760 L0 3760 Z" fill="#f3f4f8"/>
  <path d="M0 3712 C250 3760 550 3710 850 3745 C1000 3762 1120 3745 1200 3725 L1200 3800 L0 3800 Z" fill="#fff"/>
  <!-- hero photo area with wavy edge -->
  <path d="M440 0 L1200 0 L1200 430 C1180 420 1150 600 1100 614 C1000 630 900 600 780 560 C650 510 600 420 585 330 C565 220 470 140 470 60 Z" fill="#e3e5f0"/>
  <path d="M530 0 L1200 0 L1200 610 C1150 600 1080 595 980 570 C860 540 780 470 740 380 C700 290 640 200 600 130 C570 80 545 40 530 0 Z" fill="url(#heroPhoto)"/>
</svg>
<div class="abs" style="left:690px;top:90px;width:510px;height:510px" role="img" aria-label="Photo: two businessmen in a meeting, one with glasses gesturing"></div>

<!-- header -->
<div class="brand" style="left:68px;top:42px"><span class="dot"></span>Vantor Reach</div>
<nav class="nav"><span>Home</span><span>About</span><span>Services ▾</span><span>Insights</span><span>Blog</span></nav>
<div class="nav-cta">Contact Us</div>

<!-- hero -->
<h1 class="abs hero-title">Be <span class="accent">found.</span> Be <span class="accent">chosen.</span></h1>
<p class="abs hero-lead">We help business innovate and grow.</p>
<p class="abs hero-text">Specialized services for small and<br>medium sized enterprises.</p>
<div class="btn-outline" style="left:75px;top:463px;width:188px;height:50px">Learn More</div>
<svg class="abs" style="left:590px;top:575px" width="22" height="36" viewBox="0 0 22 36" aria-hidden="true"><rect x="1.5" y="1.5" width="19" height="33" rx="9.5" fill="none" stroke="#9aa0ad" stroke-width="2"/><line x1="11" y1="8" x2="11" y2="14" stroke="#9aa0ad" stroke-width="2"/></svg>

<!-- about -->
<div class="video-frame"></div>
<div class="video-card"><div class="media" role="img" aria-label="Video still: hands reviewing charts on a tablet and papers"></div></div>
<div class="play"></div>
<svg class="abs" style="left:354px;top:922px" width="28" height="30" viewBox="0 0 28 30" aria-hidden="true"><path d="M2 1 L27 15 L2 29 Z" fill="#fff"/></svg>
<div class="video-label">Vantor Reach</div>

<h2 class="section-title" style="left:687px;top:768px"><span class="bar-mark"></span>About <span class="accent" style="font-weight:500">Us</span></h2>
<div class="abs about-copy">
  <p>Vantor Reach is a playbook-as-a-service consultancy that teaches high-ticket service businesses to understand why qualified buyers don't choose them and design buying experiences where reaching full commitment is the natural conclusion.</p>
  <p><strong>We apply the tools of Revenue Psychology and Revenue Intelligence to diagnose revenue problems and design solutions.</strong></p>
</div>
<div class="btn-outline" style="left:689px;top:1077px;width:153px;height:40px;font-size:14.5px">Learn More</div>

<!-- services -->
<div class="eyebrow" style="top:1265px">What we do</div>
<div class="eyebrow" style="top:1304px;font-size:44px"><span class="accent" style="font-weight:500">Services</span> Offered</div>

<svg class="abs" style="left:130px;top:1400px" width="82" height="82" viewBox="0 0 82 82" aria-hidden="true" fill="none" stroke="var(--blue)" stroke-width="3">
  <circle cx="64" cy="16" r="12"/><path d="M64 9 v14 M60 12 h6 a3 3 0 0 1 0 6 h-4"/>
  <path d="M18 50 v-12 M28 50 v-18 M38 50 v-24 M48 50 v-16"/><path d="M14 34 L30 24 L40 28 L52 18"/>
  <path d="M4 58 h14 c10 0 18 6 22 6 h18 c4 0 4 6 0 6 H34 M4 76 h22 l36-6 c6-2 10-8 6-10"/>
</svg>
<h3 class="service-title" style="left:130px;top:1493px">Revenue Intelligence</h3>
<div class="facts" style="left:127px;top:1545px">
  <div class="fact"><h4><svg class="tick" viewBox="0 0 18 18"><circle cx="9" cy="9" r="7.5" fill="none" stroke="var(--blue)" stroke-width="1.6"/><path d="M5.5 9.2 l2.4 2.4 l4.6-4.8" fill="none" stroke="var(--blue)" stroke-width="1.6"/></svg>Definition</h4><p>The discipline of discovering and diagnosing what's actually happening in a buyer's journey before prescribing solutions.</p></div>
  <div class="fact"><h4><svg class="tick" viewBox="0 0 18 18"><circle cx="9" cy="9" r="7.5" fill="none" stroke="var(--blue)" stroke-width="1.6"/><path d="M5.5 9.2 l2.4 2.4 l4.6-4.8" fill="none" stroke="var(--blue)" stroke-width="1.6"/></svg>Metaphor</h4><p>Reconnaissance. Gathering intel on the battlefield before making strategic decisions.</p></div>
  <div class="fact"><h4><svg class="tick" viewBox="0 0 18 18"><circle cx="9" cy="9" r="7.5" fill="none" stroke="var(--blue)" stroke-width="1.6"/><path d="M5.5 9.2 l2.4 2.4 l4.6-4.8" fill="none" stroke="var(--blue)" stroke-width="1.6"/></svg>Output</h4><p>A dossier a clear-eyed assessment of reality, not assumptions.</p></div>
</div>
<div class="block" style="left:842px;top:1412px;width:224px;height:199px"></div>
<div class="photo" style="left:653px;top:1424px;width:403px;height:356px;background:linear-gradient(135deg,#1b2c4a,#2d4f8c 55%,#0f1c33)" role="img" aria-label="Photo: hands typing on a laptop with glowing data charts"></div>

<div class="block" style="left:132px;top:1931px;width:222px;height:200px"></div>
<div class="photo" style="left:142px;top:1944px;width:403px;height:354px;background:linear-gradient(135deg,#0d1426,#3a3450 50%,#1b2538)" role="img" aria-label="Photo: open hands holding a glowing AI symbol over financial charts"></div>
<svg class="abs" style="left:592px;top:1920px" width="72" height="80" viewBox="0 0 72 80" aria-hidden="true" fill="none" stroke="var(--blue)" stroke-width="3">
  <circle cx="36" cy="40" r="12"/><path d="M36 33 v14 M32 36 h6 a3 3 0 0 1 0 6 h-4"/>
  <path d="M36 4 v16 M30 10 l6-6 6 6 M14 26 a26 26 0 0 0 0 28 M58 26 a26 26 0 0 1 0 28"/>
  <path d="M4 62 h14 c8 0 14 4 18 4 h14 c4 0 4 5 0 5 H30 M4 76 h20 l30-5 c6-2 8-7 4-9"/>
</svg>
<h3 class="service-title" style="left:595px;top:2013px">Revenue Psychology</h3>
<div class="facts" style="left:592px;top:2067px">
  <div class="fact"><h4><svg class="tick" viewBox="0 0 18 18"><circle cx="9" cy="9" r="7.5" fill="none" stroke="var(--blue)" stroke-width="1.6"/><path d="M5.5 9.2 l2.4 2.4 l4.6-4.8" fill="none" stroke="var(--blue)" stroke-width="1.6"/></svg>Definition</h4><p>The discipline of applying behavioral science principles to design buying experiences where saying yes feels safer than saying no.</p></div>
  <div class="fact"><h4><svg class="tick" viewBox="0 0 18 18"><circle cx="9" cy="9" r="7.5" fill="none" stroke="var(--blue)" stroke-width="1.6"/><path d="M5.5 9.2 l2.4 2.4 l4.6-4.8" fill="none" stroke="var(--blue)" stroke-width="1.6"/></svg>Metaphor</h4><p>Decision architecture. Engineering the environment in which high-stakes choices get made.</p></div>
  <div class="fact"><h4><svg class="tick" viewBox="0 0 18 18"><circle cx="9" cy="9" r="7.5" fill="none" stroke="var(--blue)" stroke-width="1.6"/><path d="M5.5 9.2 l2.4 2.4 l4.6-4.8" fill="none" stroke="var(--blue)" stroke-width="1.6"/></svg>Output</h4><p>A design system principles and architecture for what to build, not just tactics to try.</p></div>
</div>

<!-- call to action -->
<svg class="abs" style="left:120px;top:2540px" width="330" height="330" viewBox="0 0 330 330" aria-hidden="true" fill="none" stroke="rgba(255,255,255,.22)" stroke-width="1.5">
  <circle cx="165" cy="165" r="160"/><circle cx="165" cy="165" r="135"/><circle cx="165" cy="165" r="100"/>
</svg>
<div class="abs" style="left:132px;top:2700px;width:192px;height:88px;border-radius:6px;background:linear-gradient(135deg,#ffffff,#dfe5fb)" role="img" aria-label="Illustration: white paper plane in flight"></div>
<p class="abs cta-kicker">Change starts here</p>
<h2 class="abs cta-head">Take your first step<br>towards RESULT.</h2>
<div class="cta-btn">Email us Today</div>
<div class="cta-photo" role="img" aria-label="Photo: smiling woman in a red top and jeans holding a phone"></div>

<!-- blog -->
<h2 class="section-title" style="left:0;width:1200px;text-align:center;top:3078px;font-size:44px">Latest <span class="accent" style="font-weight:500">Blog</span></h2>
<article class="card" style="left:132px">
  <div class="thumb" style="background:linear-gradient(135deg,#2a1d4f,#b0357a 60%,#2b2550)" role="img" aria-label="Photo: hands at a laptop under neon light"></div>
  <div class="body"><div class="by">By Admin</div><h3>Lorem Ipsum is simply dummy text of the printing</h3><p>There are many variations of passages of available but majority have alteration</p><a>Read More</a></div>
</article>
<article class="card" style="left:456px">
  <div class="thumb" style="background:linear-gradient(135deg,#c8d3e2,#3c5070 55%,#1b2436)" role="img" aria-label="Photo: businessman touching a digital data screen"></div>
  <div class="body"><div class="by">By Admin</div><h3>Lorem Ipsum is simply dummy text of the printing</h3><p>There are many variations of passages of available but majority have alteration</p><a>Read More</a></div>
</article>
<article class="card" style="left:780px">
  <div class="thumb" style="background:linear-gradient(135deg,#e6e8ec,#8c95a5 55%,#3d4452)" role="img" aria-label="Photo: man in a suit signing documents at a desk"></div>
  <div class="body"><div class="by">By Admin</div><h3>Lorem Ipsum is simply dummy text of the printing</h3><p>There are many variations of passages of available but majority have alteration</p><a>Read More</a></div>
</article>
<div class="btn-dark">View all Blogs</div>

<!-- contact -->
<h2 class="contact-title">Get In Touch</h2>
<div class="field" style="left:272px;top:3895px;width:315px;height:44px">Your Name</div>
<div class="field" style="left:272px;top:3966px;width:315px;height:44px">Email</div>
<div class="field" style="left:272px;top:4037px;width:315px;height:46px">Phone</div>
<div class="field" style="left:612px;top:3895px;width:314px;height:188px">Message</div>
<div class="send">Email us</div>

<!-- footer -->
<footer class="footer">
  <div class="footer-brand">Vantor Reach</div>
  <h5 style="left:473px;top:62px">COMPANY</h5>
  <ul class="footer-links"><li>Home</li><li>About Us</li><li>Services</li><li>Insights</li><li>Blog</li><li>Contact Us</li></ul>
  <h5 style="left:723px;top:56px">SUBSCRIBE</h5>
  <p class="sub-note">Subscribe to newsletter</p>
  <div class="sub-form"><span>Email address</span><b>Subscribe</b></div>
  <div class="social"><i></i><i></i><i></i><i></i></div>
  <p class="copyright">© 2026 <b>Vantor Reach</b>. All Rights Reserved.</p>
</footer>

</body>
</html>
```